I need a website built for my modeling agency company.

On our website, a user can create a profile and we will submit it to thousands of modeling agents throughout the country.

In many cases, they will receive multiple offers from modeling agencies which allows them to pick and choose the contract that is best for them to launch their modeling career.

Some tag lines to consider using:

"Submit your profile to hundreds of modeling agents instantly!"

"Get found and become a star!"

We are: The Runway Guild.

Our Slogan: The World''s Largest Network of Fashion Models and Agents

What We Do: We are an agency with one of the largest networks of fashion professionals that are looking for new modeling talent. We host professional profiles for aspiring models, professional fashion models seeking work, modeling talent seekers, and top modeling agencies. We connect aspiring models with the top modeling agencies in the United States and abroad.

By submitting your FREE profile, you will be instantly introduced to the industry’s leading modeling agents. Within a few days, you could receive multiple, competing offers from modeling agencies that all want to launch your modeling career. Receiving multiple signing offers puts you in control of deciding which contract best suites you!

Reason: I've seen some good designs, but none that are 100% perfect. These are the ones that I like best so far (to give you some ideas): http://files.pixelvane.example/img/510372/820114/820114_4917263_510372_image.jpg http://files.pixelvane.example/img/510372/829305/829305_4926851_510372_image.jpg http://files.pixelvane.example/img/510372/51847/51847_4924097_510372_image.jpg http://files.pixelvane.example/img/510372/51847/51847_4919856_510372_image.jpg http://files.pixelvane.example/img/510372/823670/823670_4920438_510372_image.jpg

Target Market(s)

Aspiring models (mostly female, but some male)

Industry/Entity Type

Modeling Agency

Colors

Designer to choose colors to be used in the design.

Requirements
Nice to have
• Somewhere in the top half of the page, I would like there to be a small form for the visitor to fill out. This form will look as follows:

Title: Instantly contact hundreds of modeling agents who are looking for new talent and could make you a star!
Fields: First Name*, Last Name*, Age, Zip Code, Email Address*, Daytime Phone, Evening Phone, Comments.

Then, there will be a "submit" button to proceed to next step of form. Just below the "submit" button, should be the following verbiage: "You will have the opportunity to upload photo(s) and provide other pertinent information in next step."

```html
<!DOCTYPE html>
<html lang="en">
<head>
<meta charset="utf-8">
<title>The Runway Guild</title>
<link href="https://fonts.googleapis.com/css2?family=Open+Sans:wght@400;600;700;800&display=swap" rel="stylesheet">
<style>
:root{
  --teal:#35b3b0;
  --teal-dark:#2a918f;
  --pink:#e9336f;
  --ink:#2b2b2b;
  --text:#555;
  --muted:#8a8a8a;
  --band:#f0f0f0;
  --card:#ffffff;
  --line:#dcdcdc;
  --dark:#262626;
}
*{box-sizing:border-box;margin:0;padding:0}
html,body{width:692px;height:1200px;overflow:hidden}
body{background:#fff;font-family:"Open Sans",Arial,sans-serif;color:var(--text);font-size:8px}
.site{position:relative;width:692px;height:1200px;background:#fff;overflow:hidden}

/* header */
.header{position:relative;height:80px}
.brand{position:absolute;left:46px;top:18px;display:flex;align-items:center;gap:8px}
.brand-mark{width:30px;height:30px;border-radius:50%;background:var(--pink)}
.brand-name{font-size:18px;font-weight:700;color:var(--ink);line-height:1}
.brand-sub{font-size:6.5px;color:var(--muted);margin-top:4px}
.account{position:absolute;right:46px;top:14px;font-size:7px;color:var(--muted);display:flex;gap:10px}
.nav{position:absolute;right:46px;top:38px;width:346px;height:22px;background:var(--teal);display:flex;justify-content:space-around;align-items:center}
.nav a{color:#fff;font-size:7px;font-weight:600;letter-spacing:.4px;padding:7px 10px}
.nav a.active{background:var(--teal-dark)}

/* hero */
.hero{position:absolute;left:46px;top:80px;width:600px;height:290px;overflow:hidden}
.hero-visual{position:absolute;inset:0;background:
  radial-gradient(ellipse 70px 95px at 67% 42%,#e6c7ad 0%,#cfa98c 45%,rgba(207,169,140,0) 100%),
  radial-gradient(ellipse 120px 70px at 70% 12%,#1d2024 0%,#2a2e34 55%,rgba(42,46,52,0) 100%),
  radial-gradient(ellipse 110px 120px at 80% 55%,#d7c0a2 0%,rgba(200,176,148,.7) 40%,rgba(120,120,120,0) 100%),
  radial-gradient(ellipse 220px 70px at 78% 100%,#3fb9c4 0%,#2c9aa8 45%,rgba(44,154,168,0) 100%),
  radial-gradient(ellipse 240px 220px at 30% 50%,#4e6478 0%,#34465a 60%,#26323f 100%)}
.hero-panel{position:absolute;left:42px;top:10px;width:206px}
.hero-title{color:#fff;font-size:9px;font-weight:700;letter-spacing:.3px;margin-bottom:6px}
.tag-row{display:flex;height:22px}
.tag{display:flex;align-items:center;justify-content:center;font-size:7px;font-weight:700;color:#fff;padding:0 6px}
.tag-pink{background:var(--pink);width:54px;line-height:1.1;text-align:center}
.tag-teal{background:var(--teal);flex:1;gap:6px}
.tag-call{background:#fff;color:var(--pink);padding:1px 5px;border-radius:2px}
.form{background:#fff;padding:8px 10px 10px}
.form-title{font-size:6.5px;color:var(--text);line-height:1.35;margin-bottom:5px}
.form-title em{color:var(--pink);font-style:normal;font-weight:700}
.fields{display:grid;grid-template-columns:1fr 1fr;gap:4px}
.field{height:13px;border:1px solid var(--line);font-size:5.5px;color:var(--muted);padding:2px 4px;background:#fafafa}
.field.wide{height:26px}
.submit-row{display:flex;align-items:flex-start;gap:6px;margin-top:6px}
.submit{background:var(--teal);color:#fff;font-size:6.5px;font-weight:700;padding:3px 9px;flex:none}
.note{font-size:5.5px;color:var(--muted);line-height:1.3}
.dots{position:absolute;left:46px;top:374px;display:flex;gap:2px}
.dots span{width:7px;height:7px;background:#bbb}
.dots span.on{background:var(--teal)}

/* photo tones */
.ph-a{background:radial-gradient(ellipse 35% 45% at 50% 45%,#d9c2b2,rgba(217,194,178,0) 100%),linear-gradient(#f2f2f2,#bdb7b2 60%,#3a3634)}
.ph-b{background:radial-gradient(ellipse 35% 45% at 50% 40%,#caa690,rgba(202,166,144,0) 100%),linear-gradient(#eae8e6,#5a4e48 75%,#2f2a28)}
.ph-c{background:radial-gradient(ellipse 35% 45% at 52% 45%,#e4c7ae,rgba(228,199,174,0) 100%),linear-gradient(#f4f4f4,#d9d4cf 50%,#9ab7c8)}
.ph-d{background:radial-gradient(ellipse 40% 55% at 50% 40%,#b89078,rgba(184,144,120,0) 100%),linear-gradient(#2c2624,#4a3a34)}
.ph-e{background:radial-gradient(ellipse 35% 50% at 50% 45%,#c99b82,rgba(201,155,130,0) 100%),linear-gradient(#f6f6f6,#e2e2e2)}
.ph-f{background:radial-gradient(ellipse 40% 45% at 50% 50%,#b3aaa3,rgba(179,170,163,0) 100%),linear-gradient(#e6e6e6,#8d8d8d 60%,#4a4a4a)}
.ph-g{background:radial-gradient(ellipse 40% 55% at 55% 45%,#d8b468,rgba(216,180,104,0) 100%),linear-gradient(#f3eee6,#c2a46e)}
.ph-h{background:radial-gradient(ellipse 30% 40% at 50% 35%,#caa08a,rgba(202,160,138,0) 100%),linear-gradient(#f2f2f2,#1e1e1e 80%)}
.ph-i{background:radial-gradient(ellipse 30% 40% at 50% 30%,#d0a88e,rgba(208,168,142,0) 100%),linear-gradient(#f0f0f0,#1f2326 85%)}
.ph-j{background:radial-gradient(ellipse 30% 40% at 50% 30%,#c9a28a,rgba(201,162,138,0) 100%),linear-gradient(#f4f4f4,#a7afbb 60%,#5b6574)}
.ph-k{background:radial-gradient(ellipse 30% 35% at 50% 30%,#d2aa90,rgba(210,170,144,0) 100%),linear-gradient(#f2f5f0,#3fae4a 70%,#2e8a38)}

/* categories */
.categories{position:absolute;left:0;top:392px;width:692px;height:214px;background:var(--band);display:flex;justify-content:center;gap:12px;padding-top:32px}
.cat{width:164px;height:182px;background:var(--card);border:1px solid var(--line);padding:6px}
.cat-label{text-align:center;font-size:8px;font-weight:600;color:var(--ink);border-bottom:1px solid var(--line);padding-bottom:5px;margin-bottom:5px;letter-spacing:.4px}
.cat-photo{height:88px}
.cat-foot{display:flex;align-items:center;margin-top:6px}
.price{background:var(--pink);color:#fff;font-size:5px;font-weight:700;padding:3px 5px;width:58px;line-height:1.3}
.price b{font-size:8px;display:block}
.see{margin-left:auto;font-size:7px;color:var(--muted);font-weight:600;display:flex;align-items:center;gap:5px}
.see i{width:10px;height:10px;border-radius:50%;background:var(--teal);display:block}

/* top models */
.top{position:absolute;left:46px;top:618px;width:600px}
.section-head{display:flex;justify-content:space-between;align-items:center;border-bottom:1px solid var(--line);padding-bottom:5px;margin-bottom:12px}
.section-title{font-size:9px;font-weight:700;color:var(--ink);letter-spacing:.3px}
.arrows{display:flex;gap:2px}
.arrows span{width:10px;height:10px;background:#ccc}
.arrows span.on{background:var(--teal)}
.grid{display:grid;grid-template-columns:repeat(5,1fr);gap:10px 12px}
.model{border:1px solid var(--line);background:#fff}
.model-photo{height:76px}
.model-info{display:flex;align-items:center;padding:4px 5px}
.model-name{font-size:5.5px;color:var(--ink);font-weight:600;line-height:1.4}
.model-name span{display:block;color:var(--pink);font-weight:400}
.tick{margin-left:auto;width:12px;height:12px}

/* call bar */
.callbar{position:absolute;left:0;top:900px;width:692px;height:36px;background:#f4f4f4;border-top:1px solid var(--line);border-bottom:1px solid var(--line);display:flex;align-items:center;padding:0 46px;gap:10px}
.icon-dark{width:18px;height:18px;border-radius:50%;background:var(--dark);display:flex;align-items:center;justify-content:center}
.call-text{font-size:7px;font-weight:700;color:var(--ink)}
.clients{margin-left:auto;display:flex;align-items:center;gap:14px;font-size:7px;font-weight:700;color:var(--ink)}
.client{font-size:7px;font-weight:600;color:var(--muted)}

/* lower */
.lower{position:absolute;left:46px;top:950px;width:600px;display:flex;gap:36px}
.speak{width:300px}
.speak p{font-size:6.5px;line-height:1.5;margin-bottom:8px}
.speak p b{color:var(--ink)}
.more{display:inline-block;background:var(--teal);color:#fff;font-size:7px;font-weight:700;padding:4px 10px;margin-top:14px}
.follow{flex:1}
.page-box{display:flex;align-items:center;gap:6px;margin-bottom:8px;font-size:6px;color:var(--muted)}
.page-box i{width:18px;height:18px;background:var(--teal);display:block}
.faces{display:grid;grid-template-columns:repeat(4,44px);gap:6px}
.face{width:44px;height:44px}

/* footer */
.footer{position:absolute;left:0;top:1140px;width:692px;height:60px;background:var(--dark);display:flex;align-items:center;padding:0 46px;color:#aaa;font-size:6.5px}
.social{margin-left:auto;display:flex;align-items:center;gap:6px}
.social i{width:14px;height:14px;border-radius:50%;background:#3a83b8;display:block}
.social i.alt{background:var(--teal)}
</style>
</head>
<body>
<div class="site">

  <header class="header">
    <div class="brand">
      <span class="brand-mark"></span>
      <div>
        <div class="brand-name">The Runway Guild</div>
        <div class="brand-sub">The World's Largest Network of Fashion Models and Agents</div>
      </div>
    </div>
    <div class="account"><span>Login</span><span>Register</span></div>
    <nav class="nav">
      <a class="active">HOME</a><a>ABOUT</a><a>MODELS</a><a>GALLERY</a><a>CONTACT</a>
    </nav>
  </header>

  <section class="hero">
    <div class="hero-visual" role="img" aria-label="Fashion model in a wide-brim black hat and turquoise top"></div>
    <div class="hero-panel">
      <div class="hero-title">THE RUNWAY GUILD</div>
      <div class="tag-row">
        <div class="tag tag-pink">OUR TOP MODELS</div>
        <div class="tag tag-teal">AGENT # 1 ST CHOICE <span class="tag-call">CALL NOW</span></div>
      </div>
      <form class="form">
        <p class="form-title">Instantly contact hundreds of modeling agents who are looking for new talent and could make you a <em>STAR!</em></p>
        <div class="fields">
          <div class="field">First Name*</div><div class="field">Last Name*</div>
          <div class="field">Age</div><div class="field">Zip Code</div>
          <div class="field">Email Address*</div><div class="field">Daytime Phone</div>
          <div class="field">Evening Phone</div><div></div>
          <div class="field wide">Comments</div>
        </div>
        <div class="submit-row">
          <span class="submit">Next »</span>
          <span class="note">You will have the opportunity to upload photo(s) and provide other pertinent information in next step.</span>
        </div>
      </form>
    </div>
  </section>
  <div class="dots"><span class="on"></span><span></span><span></span></div>

  <section class="categories">
    <div class="cat">
      <div class="cat-label">FEMALE MODELS</div>
      <div class="cat-photo ph-a" role="img" aria-label="Female model portrait in black and white"></div>
      <div class="cat-foot"><div class="price">MODELS PER MONTH<b>30 | $234</b></div><span class="see">SEE MORE <i></i></span></div>
    </div>
    <div class="cat">
      <div class="cat-label">MALE MODELS</div>
      <div class="cat-photo ph-b" role="img" aria-label="Male model in a dark jacket"></div>
      <div class="cat-foot"><div class="price">MODELS PER MONTH<b>30 | $52</b></div><span class="see">SEE MORE <i></i></span></div>
    </div>
    <div class="cat">
      <div class="cat-label">CHILD MODELS</div>
      <div class="cat-photo ph-c" role="img" aria-label="Child model in a light shirt"></div>
      <div class="cat-foot"><div class="price">MODELS PER MONTH<b>30 | $12</b></div><span class="see">SEE MORE <i></i></span></div>
    </div>
  </section>

  <section class="top">
    <div class="section-head"><span class="section-title">TOP MODELS</span><span class="arrows"><span></span><span class="on"></span></span></div>
    <div class="grid">
      <div class="model"><div class="model-photo ph-d" role="img" aria-label="Model portrait"></div><div class="model-info"><div class="model-name">Models Name<span>Since - 2013</span></div><svg class="tick" viewBox="0 0 12 12"><circle cx="6" cy="6" r="6" fill="#35b3b0"/><path d="M3.3 6.2l1.8 1.8 3.6-3.7" stroke="#fff" stroke-width="1.3" fill="none"/></svg></div></div>
      <div class="model"><div class="model-photo ph-e" role="img" aria-label="Model portrait"></div><div class="model-info"><div class="model-name">Models Name<span>Since - 2013</span></div><svg class="tick" viewBox="0 0 12 12"><circle cx="6" cy="6" r="6" fill="#35b3b0"/><path d="M3.3 6.2l1.8 1.8 3.6-3.7" stroke="#fff" stroke-width="1.3" fill="none"/></svg></div></div>
      <div class="model"><div class="model-photo ph-f" role="img" aria-label="Model portrait"></div><div class="model-info"><div class="model-name">Models Name<span>Since - 2013</span></div><svg class="tick" viewBox="0 0 12 12"><circle cx="6" cy="6" r="6" fill="#35b3b0"/><path d="M3.3 6.2l1.8 1.8 3.6-3.7" stroke="#fff" stroke-width="1.3" fill="none"/></svg></div></div>
      <div class="model"><div class="model-photo ph-g" role="img" aria-label="Model portrait"></div><div class="model-info"><div class="model-name">Models Name<span>Since - 2013</span></div><svg class="tick" viewBox="0 0 12 12"><circle cx="6" cy="6" r="6" fill="#35b3b0"/><path d="M3.3 6.2l1.8 1.8 3.6-3.7" stroke="#fff" stroke-width="1.3" fill="none"/></svg></div></div>
      <div class="model"><div class="model-photo ph-c" role="img" aria-label="Model portrait"></div><div class="model-info"><div class="model-name">Models Name<span>Since - 2013</span></div><svg class="tick" viewBox="0 0 12 12"><circle cx="6" cy="6" r="6" fill="#35b3b0"/><path d="M3.3 6.2l1.8 1.8 3.6-3.7" stroke="#fff" stroke-width="1.3" fill="none"/></svg></div></div>
      <div class="model"><div class="model-photo ph-h" role="img" aria-label="Model in a black hat"></div><div class="model-info"><div class="model-name">Models Name<span>Since - 2013</span></div><svg class="tick" viewBox="0 0 12 12"><circle cx="6" cy="6" r="6" fill="#35b3b0"/><path d="M3.3 6.2l1.8 1.8 3.6-3.7" stroke="#fff" stroke-width="1.3" fill="none"/></svg></div></div>
      <div class="model"><div class="model-photo ph-i" role="img" aria-label="Model in a black dress"></div><div class="model-info"><div class="model-name">Models Name<span>Since - 2013</span></div><svg class="tick" viewBox="0 0 12 12"><circle cx="6" cy="6" r="6" fill="#35b3b0"/><path d="M3.3 6.2l1.8 1.8 3.6-3.7" stroke="#fff" stroke-width="1.3" fill="none"/></svg></div></div>
      <div class="model"><div class="model-photo ph-b" role="img" aria-label="Model in a dark suit"></div><div class="model-info"><div class="model-name">Models Name<span>Since - 2013</span></div><svg class="tick" viewBox="0 0 12 12"><circle cx="6" cy="6" r="6" fill="#35b3b0"/><path d="M3.3 6.2l1.8 1.8 3.6-3.7" stroke="#fff" stroke-width="1.3" fill="none"/></svg></div></div>
      <div class="model"><div class="model-photo ph-j" role="img" aria-label="Model in a grey suit"></div><div class="model-info"><div class="model-name">Models Name<span>Since - 2013</span></div><svg class="tick" viewBox="0 0 12 12"><circle cx="6" cy="6" r="6" fill="#35b3b0"/><path d="M3.3 6.2l1.8 1.8 3.6-3.7" stroke="#fff" stroke-width="1.3" fill="none"/></svg></div></div>
      <div class="model"><div class="model-photo ph-k" role="img" aria-label="Model in a green jacket"></div><div class="model-info"><div class="model-name">Models Name<span>Since - 2013</span></div><svg class="tick" viewBox="0 0 12 12"><circle cx="6" cy="6" r="6" fill="#35b3b0"/><path d="M3.3 6.2l1.8 1.8 3.6-3.7" stroke="#fff" stroke-width="1.3" fill="none"/></svg></div></div>
    </div>
  </section>

  <section class="callbar">
    <span class="icon-dark"><svg width="10" height="10" viewBox="0 0 10 10"><path d="M2 1l2 2-1 1.2c.6 1.2 1.5 2.1 2.8 2.8L7 6l2 2-1.2 1.5C4.5 9.3.7 5.5.5 2.2z" fill="#fff"/></svg></span>
    <span class="call-text">CALL US FOR HELP : 1 800 555 0142</span>
    <div class="clients">
      <span class="icon-dark"><svg width="10" height="10" viewBox="0 0 10 10"><circle cx="5" cy="3.3" r="2" fill="#fff"/><path d="M1.5 9.5c0-2.2 1.6-3.5 3.5-3.5s3.5 1.3 3.5 3.5z" fill="#fff"/></svg></span>
      OUR CLIENTS:
      <span class="client">Norvale</span><span class="client">Quenby</span><span class="client">Tessaro</span>
    </div>
  </section>

  <section class="lower">
    <div class="speak">
      <div class="section-head"><span class="section-title">MODEL'S SPEAK</span></div>
      <p><b>Lorem ipsum dolor sit amet,</b> consectetur adipiscing elit, sed do eiusmod tempor incididunt ut labore et dolore magna aliqua.</p>
      <p><b>Lorem ipsum dolor sit amet,</b> consectetur adipiscing elit, sed do eiusmod tempor incididunt ut labore et dolore magna aliqua.</p>
      <span class="more">MORE</span>
    </div>
    <div class="follow">
      <div class="section-head"><span class="section-title">FOLLOW US</span></div>
      <div class="page-box"><i></i><div>Guild Page<br>123123 Likes</div></div>
      <div class="faces">
        <div class="face ph-d" role="img" aria-label="Follower photo"></div>
        <div class="face ph-e" role="img" aria-label="Follower photo"></div>
        <div class="face ph-b" role="img" aria-label="Follower photo"></div>
        <div class="face ph-c" role="img" aria-label="Follower photo"></div>
        <div class="face ph-f" role="img" aria-label="Follower photo"></div>
        <div class="face ph-i" role="img" aria-label="Follower photo"></div>
        <div class="face ph-g" role="img" aria-label="Follower photo"></div>
        <div class="face ph-a" role="img" aria-label="Follower photo"></div>
      </div>
    </div>
  </section>

  <footer class="footer">
    <span>Copyright©2013, Company Name</span>
    <div class="social">Follow Us <i></i><i class="alt"></i><i></i></div>
  </footer>

</div>
</body>
</html>
```